Real Estate Development Company Stationary

We need our company, business card, letterhead, pocket folder and envelope designed.

We are a new real estate development company. We focus on data centre, commercial and real estate development.

Please see attached for our logo. Since it's a new logo, you still can make minor adjust if you like it makes senses

The client has sent me a business card he really likes. Please see file 3.

Target Market(s)

Real Estate Investors
Large corporations
Home buyers

Industry/Entity Type

Real Estate

```html
<!DOCTYPE html>
<html lang="en">
<head>
<meta charset="utf-8">
<title>Quellbrook Development Inc. — Stationery Set</title>
<link rel="stylesheet" href="https://fonts.googleapis.com/css2?family=Montserrat:wght@600&display=swap">
<style>
  :root {
    --green: #72be44;
    --navy: #1b3f8b;
    --paper: #ffffff;
    --backdrop: #e6e8eb;
    --shadow: 0 6px 18px rgba(0,0,0,.18);
  }
  * { box-sizing: border-box; margin: 0; padding: 0; }
  html, body { width: 1200px; height: 900px; overflow: hidden; }
  body {
    background: var(--backdrop);
    font-family: "Montserrat", Arial, sans-serif;
    position: relative;
  }
  .piece {
    position: absolute;
    background: var(--paper);
    box-shadow: var(--shadow);
    overflow: hidden;
  }
  .piece > svg { position: absolute; inset: 0; width: 100%; height: 100%; }

  .brand {
    position: absolute;
    display: flex;
    align-items: center;
    gap: 7px;
    white-space: nowrap;
  }
  .brand__mark {
    width: 12px; height: 12px;
    border-radius: 50%;
    background: var(--green);
    flex: none;
  }
  .brand__name {
    color: var(--navy);
    font-weight: 600;
    font-size: 13px;
    letter-spacing: .4px;
    line-height: 1;
  }
  .brand--small { gap: 5px; }
  .brand--small .brand__mark { width: 7px; height: 7px; }
  .brand--small .brand__name { font-size: 7.5px; letter-spacing: .2px; }

  .folder      { left: 60px;  top: 150px; width: 340px; height: 480px; }
  .letterhead  { left: 440px; top: 150px; width: 340px; height: 480px; }
  .envelope    { left: 820px; top: 150px; width: 320px; height: 150px; }
  .compliment  { left: 820px; top: 330px; width: 320px; height: 150px; }
  .card-front  { left: 820px; top: 520px; width: 150px; height: 90px; }
  .card-back   { left: 990px; top: 520px; width: 150px; height: 90px; }

  .folder .brand     { left: 26px; bottom: 36px; }
  .letterhead .brand { right: 50px; top: 28px; }
  .envelope .brand   { left: 70px; top: 68px; }
  .compliment .brand { left: 24px; top: 18px; }
  .card-front .brand { left: 10px; top: 12px; }
  .card-back .brand  { left: 16px; top: 40px; }
</style>
</head>
<body>

  <section class="piece folder" aria-label="Pocket folder">
    <svg viewBox="0 0 340 480" preserveAspectRatio="none">
      <path d="M0 0 H340 V60 C260 70 215 115 195 185 C170 270 90 335 0 350 Z" fill="var(--green)"/>
      <path d="M340 62 C262 72 218 117 198 187 C173 272 92 338 0 353" fill="none" stroke="var(--navy)" stroke-width="4"/>
      <path d="M340 70 C268 80 226 124 206 192 C181 278 100 345 0 362" fill="none" stroke="var(--green)" stroke-width="2"/>
    </svg>
    <div class="brand">
      <span class="brand__mark"></span>
      <span class="brand__name">Quellbrook Development Inc.</span>
    </div>
  </section>

  <section class="piece letterhead" aria-label="Letterhead">
    <svg viewBox="0 0 340 480" preserveAspectRatio="none">
      <path d="M285 0 H340 V55 C330 28 310 8 285 0 Z" fill="var(--green)"/>
      <path d="M0 330 C100 385 230 400 340 380 V480 H0 Z" fill="var(--green)"/>
      <path d="M0 330 C100 385 230 400 340 380" fill="none" stroke="var(--navy)" stroke-width="4"/>
    </svg>
    <div class="brand">
      <span class="brand__mark"></span>
      <span class="brand__name">Quellbrook Development Inc.</span>
    </div>
  </section>

  <section class="piece envelope" aria-label="Envelope">
    <svg viewBox="0 0 320 150" preserveAspectRatio="none">
      <path d="M150 0 H320 V34 C300 30 210 22 150 0 Z" fill="var(--green)"/>
    </svg>
    <div class="brand">
      <span class="brand__mark"></span>
      <span class="brand__name">Quellbrook Development Inc.</span>
    </div>
  </section>

  <section class="piece compliment" aria-label="Compliment slip">
    <svg viewBox="0 0 320 150" preserveAspectRatio="none">
      <rect width="320" height="150" fill="var(--green)"/>
      <ellipse cx="160" cy="75" rx="178" ry="92" fill="var(--paper)" stroke="var(--navy)" stroke-width="3"/>
    </svg>
    <div class="brand brand--small">
      <span class="brand__mark"></span>
      <span class="brand__name">Quellbrook Development Inc.</span>
    </div>
  </section>

  <section class="piece card-front" aria-label="Business card front">
    <svg viewBox="0 0 150 90" preserveAspectRatio="none">
      <path d="M0 48 C50 58 110 52 150 40 V90 H0 Z" fill="var(--green)"/>
      <path d="M0 48 C50 58 110 52 150 40" fill="none" stroke="var(--navy)" stroke-width="2"/>
    </svg>
    <div class="brand brand--small">
      <span class="brand__mark"></span>
      <span class="brand__name">Quellbrook Development Inc.</span>
    </div>
  </section>

  <section class="piece card-back" aria-label="Business card back">
    <div class="brand brand--small">
      <span class="brand__mark"></span>
      <span class="brand__name">Quellbrook Development Inc.</span>
    </div>
  </section>

</body>
</html>
```